Design some Business Cards for Tavro

Thanks to everyone for their efforts. I will just be reviewing the first two entries from each contestant, so I'd suggest withdrawing entries which are not your favorites & going with your best two. Many thanks, Derek

I was after a double sided business card for tavro.com.au. Tavro is a billing app and website for tradesman and service providers who move from site to site.

Firstly design for Derek Holm with mobile 0481 555 907 & email demo@tavro.com.au.

Logo is attached, so please work with those colours. I've also included our url if you believe that is worth building in.

I would like the original working files and the business card will need to be produced for 3 different employees when the winner is selected.

Additional TAVRO text files if this helps.

```html
<!DOCTYPE html>
<html lang="en">
<head>
<meta charset="utf-8">
<title>Tavro Business Cards</title>
<link rel="stylesheet" href="https://fonts.googleapis.com/css2?family=Open+Sans:wght@400;600;700&display=swap">
<style>
  :root {
    --stage: #3a3a3a;
    --card: #ffffff;
    --brand-blue: #2ea3dc;
    --band-blue: #3fb0e6;
    --accent-red: #d8262d;
    --ink: #2b2b2b;
    --shadow: rgba(0, 0, 0, 0.45);
  }
  * { box-sizing: border-box; margin: 0; padding: 0; }
  html, body {
    width: 1200px;
    height: 851px;
    overflow: hidden;
  }
  body {
    background: var(--stage);
    font-family: "Open Sans", Arial, sans-serif;
    position: relative;
  }
  .card {
    position: absolute;
    top: 275px;
    width: 520px;
    height: 300px;
    background: var(--card);
    border-radius: 22px;
    overflow: hidden;
    box-shadow: 0 14px 30px var(--shadow);
  }
  .card-front { left: 50px; }
  .card-back { left: 630px; }

  .brand {
    position: absolute;
    display: flex;
    align-items: center;
    gap: 14px;
  }
  .brand-dot {
    border-radius: 50%;
    background: var(--brand-blue);
  }
  .brand-name {
    font-weight: 700;
    color: var(--brand-blue);
    letter-spacing: 2px;
    line-height: 1;
  }
  .card-front .brand { left: 95px; top: 100px; }
  .card-front .brand-dot { width: 58px; height: 58px; }
  .card-front .brand-name { font-size: 62px; }

  .front-url {
    position: absolute;
    left: 150px;
    top: 196px;
    font-size: 14px;
    font-weight: 600;
    color: var(--brand-blue);
    letter-spacing: 1.5px;
  }

  .card-back .brand { left: 32px; top: 58px; }
  .card-back .brand-dot { width: 46px; height: 46px; }
  .card-back .brand-name { font-size: 46px; color: var(--ink); }

  .person {
    position: absolute;
    left: 318px;
    top: 118px;
  }
  .person-name {
    font-size: 23px;
    font-weight: 700;
    color: var(--accent-red);
    line-height: 1.1;
  }
  .person-role {
    font-size: 18px;
    color: var(--brand-blue);
    line-height: 1.2;
  }
  .contacts {
    list-style: none;
    margin-top: 14px;
    margin-left: -18px;
  }
  .contacts li {
    display: flex;
    align-items: center;
    gap: 7px;
    font-size: 15px;
    color: var(--ink);
    line-height: 21px;
  }
  .contacts svg { width: 12px; height: 12px; flex: none; }

  .back-rule {
    position: absolute;
    left: 0; right: 0;
    bottom: 32px;
    height: 4px;
    background: var(--accent-red);
  }
  .back-band {
    position: absolute;
    left: 0; right: 0;
    bottom: 0;
    height: 32px;
    background: var(--band-blue);
  }
</style>
</head>
<body>
  <section class="card card-front">
    <div class="brand">
      <span class="brand-dot"></span>
      <span class="brand-name">TAVRO</span>
    </div>
    <p class="front-url">WWW.TAVRO.COM.AU</p>
  </section>

  <section class="card card-back">
    <div class="brand">
      <span class="brand-dot"></span>
      <span class="brand-name">TAVRO</span>
    </div>
    <div class="person">
      <p class="person-name">Derek Holm</p>
      <p class="person-role">Director</p>
      <ul class="contacts">
        <li>
          <svg viewBox="0 0 12 12" aria-hidden="true"><circle cx="6" cy="6" r="6" fill="#2ea3dc"/><path d="M4 3.2 5 3l.6 1.5-.7.5a4 4 0 0 0 2 2l.5-.7L9 6.9l-.2 1a1 1 0 0 1-1 .7A5 5 0 0 1 3.3 4.2a1 1 0 0 1 .7-1z" fill="#fff"/></svg>
          0481 555 907
        </li>
        <li>
          <svg viewBox="0 0 12 12" aria-hidden="true"><circle cx="6" cy="6" r="6" fill="#2ea3dc"/><rect x="3" y="4" width="6" height="4.2" fill="#fff"/><path d="M3 4 6 6.4 9 4" fill="none" stroke="#2ea3dc" stroke-width=".8"/></svg>
          derek@tavro.com.au
        </li>
        <li>
          <svg viewBox="0 0 12 12" aria-hidden="true"><circle cx="6" cy="6" r="6" fill="#2ea3dc"/><circle cx="6" cy="6" r="3.3" fill="none" stroke="#fff" stroke-width=".8"/><path d="M2.7 6h6.6M6 2.7c-1.6 2-1.6 4.6 0 6.6M6 2.7c1.6 2 1.6 4.6 0 6.6" fill="none" stroke="#fff" stroke-width=".7"/></svg>
          www.tavro.com.au
        </li>
      </ul>
    </div>
    <div class="back-rule"></div>
    <div class="back-band"></div>
  </section>
</body>
</html>
```